Providing Back Office Solutions to Financial Advisors and Attorney Needs a Business Card Design

Need a Business Card Design that speaks to Financial Advisor and Attorneys. Some of the word that come to mind is Clean/Simple & Futuristic.

Industry/Entity Type

Business

```html
<!DOCTYPE html>
<html lang="en">
<head>
<meta charset="utf-8">
<title>Kallinos Business Card</title>
<link href="https://fonts.googleapis.com/css2?family=Montserrat:wght@400;500;700&display=swap" rel="stylesheet">
<style>
  :root {
    --page-bg: #e9eaec;
    --card-bg: #ffffff;
    --brand-blue: #1b80c0;
    --text-grey: #5a5a5a;
    --text-dark: #3c3c3c;
    --rule-grey: #b9b9b9;
  }
  * { margin: 0; padding: 0; box-sizing: border-box; }
  html, body {
    width: 1200px;
    height: 900px;
    overflow: hidden;
    background: var(--page-bg);
    font-family: "Montserrat", Arial, sans-serif;
  }
  .canvas {
    width: 1200px;
    height: 900px;
    display: flex;
    align-items: center;
    justify-content: center;
  }
  .business-card {
    position: relative;
    width: 1000px;
    height: 572px;
    background: var(--card-bg);
    box-shadow: 0 6px 24px rgba(0,0,0,0.12);
    display: flex;
    align-items: center;
  }
  .brand-block {
    width: 500px;
    display: flex;
    align-items: center;
    justify-content: center;
    gap: 18px;
  }
  .brand-square {
    width: 70px;
    height: 70px;
    background: var(--brand-blue);
  }
  .brand-name {
    color: var(--brand-blue);
    font-weight: 500;
    line-height: 1.15;
  }
  .brand-name .word {
    display: block;
    font-size: 58px;
    letter-spacing: 4px;
  }
  .brand-name .tagline {
    display: block;
    font-size: 17px;
    letter-spacing: 1.5px;
  }
  .divider {
    width: 2px;
    height: 280px;
    background: var(--rule-grey);
  }
  .contact-block {
    padding-left: 48px;
    color: var(--text-grey);
  }
  .person-name {
    font-size: 46px;
    font-weight: 700;
    color: var(--brand-blue);
    line-height: 1.05;
  }
  .person-title {
    font-size: 32px;
    font-weight: 400;
    color: var(--text-grey);
    margin-bottom: 18px;
  }
  .address {
    font-size: 21px;
    line-height: 1.35;
    color: var(--text-grey);
    margin-bottom: 16px;
  }
  .contact-list { list-style: none; }
  .contact-list li {
    display: flex;
    align-items: center;
    gap: 12px;
    font-size: 21px;
    line-height: 1.5;
    color: var(--text-dark);
  }
  .contact-list svg {
    width: 20px;
    height: 20px;
    fill: var(--brand-blue);
    flex: none;
  }
</style>
</head>
<body>
<main class="canvas">
  <section class="business-card">
    <div class="brand-block">
      <div class="brand-square"></div>
      <div class="brand-name">
        <span class="word">KALLINOS</span>
        <span class="tagline">BACK OFFICE SOLUTIONS</span>
      </div>
    </div>
    <div class="divider"></div>
    <div class="contact-block">
      <h1 class="person-name">Daniel Reeve</h1>
      <p class="person-title">President</p>
      <p class="address">42 Harlow Crest Avenue<br>Melbourne 3000</p>
      <ul class="contact-list">
        <li>
          <svg viewBox="0 0 24 24" aria-hidden="true"><path d="M6.6 10.8a15.1 15.1 0 0 0 6.6 6.6l2.2-2.2a1 1 0 0 1 1-.25 11.4 11.4 0 0 0 3.6.57 1 1 0 0 1 1 1V20a1 1 0 0 1-1 1A17 17 0 0 1 3 4a1 1 0 0 1 1-1h3.5a1 1 0 0 1 1 1c0 1.25.2 2.45.57 3.57a1 1 0 0 1-.25 1z"/></svg>
          555 018 4472
        </li>
        <li>
          <svg viewBox="0 0 24 24" aria-hidden="true"><path d="M2 5h20v14H2z" fill="none"/><path d="M2 5h20v2l-10 6L2 7zM2 9l10 6 10-6v10H2z"/></svg>
          info@kallinosbo.com
        </li>
        <li>
          <svg viewBox="0 0 24 24" aria-hidden="true"><circle cx="12" cy="12" r="9" fill="none" stroke="#1b80c0" stroke-width="2"/><ellipse cx="12" cy="12" rx="4" ry="9" fill="none" stroke="#1b80c0" stroke-width="1.6"/><path d="M3 12h18M4.5 7.5h15M4.5 16.5h15" stroke="#1b80c0" stroke-width="1.6"/></svg>
          www.kallinosbo.com
        </li>
      </ul>
    </div>
  </section>
</main>
</body>
</html>
```